VornaDesk website (https://vornadesk.example) re-design

Website purposed for providing general information on products we develop and offer. Products are software specific to online poker players.
Software not playful but complex technological solutions so website should look neatly and professional.
More details on the project you may find in this document:
https://papers.quillnest.example/doc/7TmR2kZpW9xLqB4nVc8YdHs3EfGaJu6KoPi1NwXe/edit#section=s.qkmz4f81b2rn
Or below:
Technology: preferable bootstrap, but not critical
CrossPlatform: Desktop/Mobile
Pages:
Main (Current https://vornadesk.example/)
Video, Room list, Features, Price, Contacts
Partner section (whom we work with)
Documentation and FAQ links
Login (Current https://vornadesk.example/Login/Login)
SignUp/Password recovery (https://vornadesk.example/Signup/Signup, https://vornadesk.example/Login/RemindPassword)
License token (unique and assigned per customer). Need an option to copy to clipboard from Dashboard screen.
Download link for latest product version.
Subs end date to display
Manuals FAQ links
Buy and renew subscription
Notes: Group everything related to subscription into one logic block on the screen.
FAQ (https://vornadesk.example/Home/FAQ).
Simple and comfortable in usage faq.
Notes: Combine all the steps into one screen.
Make download trial which leads to registration!
Target Market(s)
Online poker players
Number of Pages Required
5+ page

```html
<!DOCTYPE html>
<html lang="en">
<head>
<meta charset="utf-8">
<title>VornaDesk</title>
<link href="https://fonts.googleapis.com/css2?family=Montserrat:wght@300;400;500;600;700;800&display=swap" rel="stylesheet">
<style>
:root{
  --navy:#0a1f7a;
  --royal:#1437a8;
  --deep:#06135a;
  --sky:#27a8e0;
  --ink:#1b1b2b;
  --white:#ffffff;
}
*{box-sizing:border-box;margin:0;padding:0}
html,body{width:1200px;height:4588px;overflow:hidden}
body{font-family:'Montserrat',sans-serif;color:var(--ink);background:var(--white);position:relative}
.abs{position:absolute}
a{color:inherit;text-decoration:none}

/* shared */
.brand{font-weight:700;color:var(--white);display:flex;align-items:center;gap:10px;white-space:nowrap}
.brand-mark{width:22px;height:22px;background:var(--white);border-radius:3px}
.nav{display:flex;gap:17px;font-size:15px;color:var(--white);font-weight:500;white-space:nowrap}
.btn-pill{display:flex;align-items:center;justify-content:center;border-radius:30px;font-weight:700}
.section-title{font-size:44px;color:var(--navy);font-weight:400;white-space:nowrap}
.section-title b{font-weight:800;color:var(--royal)}

/* hero */
.hero{left:0;top:0;width:1200px;height:716px;background:linear-gradient(120deg,#0c2a95 0%,#1a46b8 45%,#0b2380 100%)}
.site-brand{left:160px;top:28px;font-size:38px;height:50px}
.site-nav{left:533px;top:43px}
.hero-visual{left:566px;top:214px;width:634px;height:516px;border-radius:26px 0 0 0;background:linear-gradient(160deg,#e9edf3 0%,#c9d1dd 40%,#2d3b55 100%)}
.hero-title{left:158px;top:234px;font-size:62px;line-height:76px;color:var(--white);font-weight:400;white-space:nowrap;z-index:2}
.hero-title b{font-weight:800}
.hero-text{left:158px;top:415px;width:345px;font-size:14px;line-height:23px;color:var(--white);text-align:justify}
.start-trial{left:160px;top:527px;width:185px;height:51px;background:var(--white);color:var(--royal);font-size:15px}

/* intro */
.intro-title{left:0;top:785px;width:1200px;text-align:center}
.intro-text{left:300px;top:853px;width:600px;text-align:center;font-size:15px;line-height:23px}
.laptop-lid{left:263px;top:938px;width:672px;height:437px;background:#f1f2f5;border-radius:18px 18px 0 0;border:2px solid #e0e3ea}
.video{left:281px;top:966px;width:638px;height:383px;background:#050505}
.video-bar{left:281px;top:966px;width:638px;height:45px;background:#24262b}
.video-caption{left:284px;top:1083px;font-size:18px;line-height:24px;color:#4a3a00;background:#a88f00;white-space:nowrap;padding-right:4px}
.play{left:557px;top:1103px}
.laptop-base{left:183px;top:1370px;width:832px;height:18px;background:linear-gradient(#fbfbfc,#d8dbe2);border-radius:0 0 40px 40px}

/* rooms */
.rooms{left:0;top:1452px;width:1200px;height:784px;background:linear-gradient(135deg,#3a3c42 0%,#8d8f96 40%,#2e3036 70%,#6f7178 100%)}
.room{width:205px;height:187px;background:var(--white);border-radius:6px;box-shadow:0 4px 14px rgba(0,0,0,.35);display:flex;flex-direction:column;align-items:center;justify-content:flex-end;padding-bottom:22px}
.room-badge{width:82px;height:82px;border-radius:18px;margin-bottom:22px}
.room-name{font-size:14px;font-weight:600;color:var(--royal);white-space:nowrap}

/* features */
.features{left:0;top:2236px;width:1200px;height:632px;background:linear-gradient(180deg,#a9cfe0,#bcd7e4)}
.features-title{left:0;top:2337px;width:1200px;text-align:center}
.feature{width:208px;height:270px;background:var(--white);box-shadow:0 3px 12px rgba(0,0,0,.18);text-align:center;padding-top:40px}
.feature h3{font-size:15px;font-weight:700;color:var(--royal);margin-top:14px}
.feature p{font-size:11px;line-height:14px;margin:6px 20px 0}
.feature .btn-pill{width:140px;height:36px;margin:18px auto 0;border:2px solid var(--navy);color:var(--navy);font-size:11px}
.arrow{top:2568px}

/* pricing */
.pricing-title{left:160px;top:2988px}
.pricing-text{left:160px;top:3080px;width:335px;font-size:11px;line-height:18px;text-align:justify}
.pricing-text p{margin-bottom:18px}
.contact-btn{left:160px;top:3378px;width:140px;height:35px;background:var(--sky);color:var(--white);font-size:11px}
.plan{text-align:center}
.plan .price{font-size:46px;font-weight:700}
.plan .name{font-size:21px;font-weight:700;margin-top:14px}
.plan .meta{font-size:11px;line-height:22px;margin-top:8px}
.plan .btn-pill{width:140px;height:36px;margin:16px auto 0;font-size:11px}
.plan-b{left:563px;top:3048px;width:260px;height:312px;background:linear-gradient(160deg,#1a4fc4,#0a1f7a);color:var(--white);padding-top:52px;z-index:2;box-shadow:0 6px 20px rgba(0,0,0,.25)}
.plan-b .btn-pill{background:var(--white);color:var(--navy)}
.plan-a{left:808px;top:3070px;width:227px;height:275px;background:var(--white);color:var(--navy);padding-top:36px;box-shadow:0 3px 14px rgba(0,0,0,.18)}
.plan-a .meta{color:var(--ink)}
.plan-a .btn-pill{border:2px solid var(--navy);color:var(--navy)}
.pricing-note{left:565px;top:3392px;font-size:14px;white-space:nowrap}

/* contact */
.map{top:3515px;height:633px;background:linear-gradient(135deg,#eef0f1,#e2e5e7)}
.contact{left:473px;top:3515px;width:574px;height:633px;background:linear-gradient(180deg,#1a4fc4,#0a1f7a)}
.contact-title{left:473px;top:3605px;width:574px;text-align:center;font-size:44px;font-weight:700;color:var(--white)}
.contact-text{left:520px;top:3677px;width:480px;text-align:center;font-size:14px;line-height:23px;color:var(--white)}
.field{background:var(--white);font-size:9px;color:#888;padding:12px 18px}
.send{left:516px;top:3997px;width:488px;height:42px;background:var(--sky);color:var(--white);font-size:12px;font-weight:700;letter-spacing:3px;display:flex;align-items:center;justify-content:center}

/* footer */
.footer{left:0;top:4148px;width:1200px;height:440px;background:linear-gradient(135deg,#0c3fb0 0%,#0a2590 50%,#06135a 100%)}
.footer-brand{left:0;top:4228px;width:1200px;justify-content:center;font-size:44px}
.follow{left:0;top:4322px;width:1200px;text-align:center;color:var(--white);font-size:13px;font-weight:600}
.socials{left:0;top:4364px;width:1200px;display:flex;justify-content:center;gap:14px}
.socials span{width:20px;height:20px;border-radius:50%;background:var(--white)}
.footer-nav{left:0;top:4450px;width:1200px;justify-content:center}
.footer-line{left:0;top:4515px;width:1200px;height:1px;background:rgba(255,255,255,.35)}
.copyright{left:0;top:4548px;width:1200px;text-align:center;color:var(--white);font-size:10px}
</style>
</head>
<body>

<header class="abs hero"></header>
<div class="abs hero-visual" role="img" aria-label="Desktop monitor and laptop showing several poker tables with the tracking software"></div>
<div class="abs brand site-brand"><span class="brand-mark"></span>VornaDesk</div>
<nav class="abs nav site-nav"><a>Home</a><a>Rooms</a><a>Features</a><a>Price</a><a>Dashboard</a><a>FAQs</a><a>Contact Us</a></nav>
<h1 class="abs hero-title">Welcome <b>to</b><br><b>VornaDesk</b></h1>
<p class="abs hero-text">Lorem ipsum dolor sit amet, consectetur adipisicing elit, sed do eiusmod tempor incididunt ut labore et dolore magna aliqua.</p>
<a class="abs btn-pill start-trial">Start Trial</a>

<h2 class="abs section-title intro-title"><b>Introduction</b> to <b>VornaDesk</b></h2>
<p class="abs intro-text">Lorem ipsum dolor sit amet, consectetur adipisicing elit, sed do eiusmod tempor incididunt ut labore et dolore magna aliqua.</p>
<div class="abs laptop-lid"></div>
<div class="abs video"></div>
<div class="abs video-bar"></div>
<div class="abs video-caption">Setup hands history auto-import<br>for "Eastern Card Clubs" Site in<br>Stackview Manager</div>
<svg class="abs play" width="86" height="86" viewBox="0 0 86 86"><circle cx="43" cy="43" r="40" fill="#1f3b58" stroke="#0f2236" stroke-width="6"/><circle cx="43" cy="43" r="30" fill="#fff"/><path d="M35 28 L60 43 L35 58 Z" fill="#27a8e0"/></svg>
<div class="abs laptop-base"></div>

<section class="abs rooms" role="img" aria-label="Tilted screenshots of the software dashboard as background"></section>
<div class="abs room" style="left:160px;top:1570px"><span class="room-badge" style="background:#d8262a;border-radius:50%"></span><span class="room-name">Rooms &amp; Features</span></div>
<div class="abs room" style="left:385px;top:1570px"><span class="room-badge" style="background:#1d3f9a"></span><span class="room-name">CardCrest Asia</span></div>
<div class="abs room" style="left:610px;top:1570px"><span class="room-badge" style="background:#1fb89a"></span><span class="room-name">TablePeak</span></div>
<div class="abs room" style="left:835px;top:1570px"><span class="room-badge" style="background:#d6a64a;border-radius:50%"></span><span class="room-name">ChipLane</span></div>
<div class="abs room" style="left:160px;top:1775px"><span class="room-badge" style="background:#3aa76a"></span><span class="room-name">RiverHour</span></div>
<div class="abs room" style="left:385px;top:1775px"><span class="room-badge" style="background:#c9a46a;border-radius:50%"></span><span class="room-name">FlopForge</span></div>
<div class="abs room" style="left:610px;top:1775px"><span class="room-badge" style="background:#f39a1c"></span><span class="room-name">PotCircle</span></div>
<div class="abs room" style="left:835px;top:1775px"><span class="room-badge" style="background:#2bb07a;border-radius:50%"></span><span class="room-name">DealNest/KeyDeal</span></div>
<div class="abs room" style="left:160px;top:1980px"><span class="room-badge" style="background:#1d9fb0"></span><span class="room-name">ReefCards</span></div>
<div class="abs room" style="left:385px;top:1980px"><span class="room-badge" style="background:#c8a070;border-radius:50%"></span><span class="room-name">TrueStack</span></div>
<div class="abs room" style="left:610px;top:1980px"><span class="room-badge" style="background:#c9b08a;border-radius:50%"></span><span class="room-name">Rooms &amp; Features</span></div>
<div class="abs room" style="left:835px;top:1980px"><span class="room-badge" style="background:#d7262d"></span><span class="room-name">FullPush</span></div>

<section class="abs features" role="img" aria-label="Faded photo of a workspace with laptop as background"></section>
<h2 class="abs section-title features-title"><b>Our Features</b></h2>
<svg class="abs arrow" style="left:108px" width="20" height="40" viewBox="0 0 20 40"><path d="M17 3 L4 20 L17 37" fill="none" stroke="#1b1b2b" stroke-width="2"/></svg>
<svg class="abs arrow" style="left:1057px" width="20" height="40" viewBox="0 0 20 40"><path d="M3 3 L16 20 L3 37" fill="none" stroke="#1b1b2b" stroke-width="2"/></svg>

<article class="abs feature" style="left:150px;top:2445px">
  <svg width="56" height="46" viewBox="0 0 56 46"><path d="M28 2 L14 14 M28 2 L42 14" stroke="#1437a8" stroke-width="2"/><rect x="4" y="14" width="48" height="28" fill="none" stroke="#1437a8" stroke-width="2"/><rect x="10" y="20" width="36" height="10" fill="#1437a8"/></svg>
  <h3>Rooms &amp; Features</h3><p>Lorem ipsum dolor sit amet, consectetur adipisicing elit, sed do eiusmod</p><a class="btn-pill">LEARN MORE</a>
</article>
<article class="abs feature" style="left:374px;top:2488px">
  <svg width="56" height="46" viewBox="0 0 56 46"><circle cx="30" cy="14" r="11" fill="none" stroke="#1437a8" stroke-width="2"/><path d="M6 40 Q18 28 30 34 L46 30" fill="none" stroke="#1437a8" stroke-width="2"/></svg>
  <h3>Pricing &amp; Purchasing</h3><p>Lorem ipsum dolor sit amet, consectetur adipisicing elit, sed do eiusmod</p><a class="btn-pill">LEARN MORE</a>
</article>
<article class="abs feature" style="left:600px;top:2445px">
  <svg width="56" height="46" viewBox="0 0 56 46"><rect x="6" y="4" width="44" height="34" fill="none" stroke="#1437a8" stroke-width="2"/><path d="M12 32 L40 10 M16 12 L40 34" stroke="#1437a8" stroke-width="3"/></svg>
  <h3>Troubleshooting</h3><p>Lorem ipsum dolor sit amet, consectetur adipisicing elit, sed do eiusmod</p><a class="btn-pill">LEARN MORE</a>
</article>
<article class="abs feature" style="left:825px;top:2488px">
  <svg width="56" height="46" viewBox="0 0 56 46"><rect x="19" y="10" width="18" height="32" rx="3" fill="none" stroke="#1437a8" stroke-width="2"/><path d="M30 6 Q36 2 40 6 M32 2 Q40 -2 44 4" fill="none" stroke="#1437a8" stroke-width="2"/></svg>
  <h3>Trackers &amp; HUD</h3><p>Lorem ipsum dolor sit amet, consectetur adipisicing elit, sed do eiusmod</p><a class="btn-pill">LEARN MORE</a>
</article>

<h2 class="abs section-title pricing-title"><b>Our Pricing</b></h2>
<div class="abs pricing-text">
  <p>Price depends on stakes you play. We accept Paystrand, Coinvale, BTC and Quickremit. For Quickremit details please contact us. You may renew the service with "Buy or renew subscription" button on your Dashboard.</p>
  <p>You may renew the service with "Buy or renew subscription" button on your Dashboard.</p>
  <p>In case software works stable with no issues we do 50% refund for the license which is used less or equal to 14 days. Otherwise, refund is not supposed.</p>
  <p>When software is not operational or does not work as expected please contact us for assistance.</p>
</div>
<a class="abs btn-pill contact-btn">CONTACT US</a>
<div class="abs plan plan-b"><div class="price">$60</div><div class="name">Plan B</div><div class="meta">Any stakes,<br>1 month</div><a class="btn-pill">BUY NOW</a></div>
<div class="abs plan plan-a"><div class="price">$30</div><div class="name">Plan A</div><div class="meta">Stakes 2/4/8 and less,<br>1 month</div><a class="btn-pill">BUY NOW</a></div>
<p class="abs pricing-note">Note: There is no low stakes plan for DealNest and ChipLane</p>

<div class="abs map" style="left:0;width:473px" role="img" aria-label="Street map of the central region"></div>
<div class="abs map" style="left:1047px;width:153px" role="img" aria-label="Street map of the eastern region"></div>
<section class="abs contact"></section>
<h2 class="abs contact-title">CONTACT US</h2>
<p class="abs contact-text">Lorem ipsum dolor sit amet, consectetur adipisicing elit, sed do eiusmod tempor incididunt ut.</p>
<div class="abs field" style="left:516px;top:3761px;width:230px;height:38px">Name</div>
<div class="abs field" style="left:773px;top:3761px;width:231px;height:38px">Email</div>
<div class="abs field" style="left:516px;top:3814px;width:488px;height:38px">Phone</div>
<div class="abs field" style="left:516px;top:3867px;width:488px;height:120px">Message</div>
<a class="abs send">SEND</a>

<footer class="abs footer"></footer>
<div class="abs brand footer-brand"><span class="brand-mark"></span>VornaDesk</div>
<div class="abs follow">FOLLOW US</div>
<div class="abs socials"><span></span><span></span><span></span><span></span></div>
<nav class="abs nav footer-nav"><a>Home</a><a>Rooms</a><a>Features</a><a>Price</a><a>Dashboard</a><a>FAQs</a><a>Contact Us</a></nav>
<div class="abs footer-line"></div>
<p class="abs copyright">© 2019 VornaDesk. All rights Reserved</p>

</body>
</html>
```